Business Card Design for Photographer

Updating business card design. Must use included logo. We're a luxury wedding photography business. Elegancy, luxury, consistency are messages we wish to convey.

Visit our website at www.colbyvarnway.com to familiarize yourself more with our brand design currently (fonts, colors etc.). This is what we want to maintain.

Target Market(s)

Luxury Brides and Grooms

Industry/Entity Type

Wedding

Contact Information for Business Card

Current logo (attached to brief)
Name: Colby Varnway
Phone: 5208813047
website/blog
Email

Requirements
Must have
• Current logo (attached to brief)
• Name: Colby Varnway
• Phone: 5208813047
• website/blog
• Email
• Social username
Should not have
• bright colors, fonts that don't suit our brand (visit www.colbyvarnway.com)

```html
<!DOCTYPE html>
<html lang="en">
<head>
<meta charset="utf-8">
<title>Colby Varnway Photographers — Business Card</title>
<link rel="stylesheet" href="https://fonts.googleapis.com/css2?family=Josefin+Sans:wght@300;400&family=Tenor+Sans&display=swap">
<style>
  :root {
    --page: #ffffff;
    --card: #f6f7f9;
    --panel: #eeeff1;
    --band: #dfe0e2;
    --mark: #6f6f71;
    --ink: #5f6063;
    --gutter: #ffffff;
    --photo-garden: linear-gradient(135deg, #5f6b3e, #c9c9c4 70%, #e9e9e6);
    --photo-tent: linear-gradient(180deg, #eef0ee, #b7bfa9 60%, #6b7a4a);
    --photo-lane: linear-gradient(180deg, #d6dcd2, #4b5d35 45%, #7b6a5c);
    --photo-chapel: linear-gradient(180deg, #b7c4b0, #6e8060 50%, #d9dccd);
    --photo-bouquet: linear-gradient(135deg, #5a4a42, #e0a394 50%, #8a9aa0);
    --photo-beach: linear-gradient(180deg, #e4ecef, #a9c4cd 45%, #efece6);
  }
  * { margin: 0; padding: 0; box-sizing: border-box; }
  html, body { width: 1200px; height: 900px; overflow: hidden; background: var(--page); }
  body { position: relative; font-family: "Tenor Sans", sans-serif; color: var(--ink); }

  .card {
    position: absolute;
    width: 667px; height: 407px;
    background: var(--card);
    box-shadow: 2px 3px 6px rgba(0,0,0,0.18);
    overflow: hidden;
  }
  .card--front { left: 95px; top: 28px; }
  .card--back { left: 427px; top: 453px; }

  .band {
    position: absolute; left: 0; right: 0;
    background: var(--band);
  }
  .card--front .band { top: 188px; height: 186px; }
  .card--back .band { top: 192px; height: 187px; }

  /* Front */
  .brand-block {
    position: absolute; left: 195px; top: 44px;
    width: 288px; height: 121px;
    background: var(--panel);
    text-align: center;
  }
  .brand-square {
    position: absolute; left: 124px; top: 7px;
    width: 44px; height: 43px;
    background: var(--mark);
  }
  .brand-name {
    position: absolute; left: 0; right: 0; top: 64px;
    font-family: "Josefin Sans", sans-serif; font-weight: 300;
    font-size: 22px; letter-spacing: 4px; color: var(--ink);
    white-space: nowrap;
  }
  .brand-tag {
    position: absolute; left: 0; right: 0; top: 98px;
    font-family: "Josefin Sans", sans-serif; font-weight: 400;
    font-size: 11px; letter-spacing: 4px; color: var(--ink);
  }
  .gallery {
    position: absolute; left: 185px; top: 188px;
    width: 297px; height: 186px;
    background: var(--gutter);
  }
  .gallery__photo { position: absolute; }
  .photo--garden  { left: 4px;   top: 1px;  width: 142px; height: 91px; background: var(--photo-garden); }
  .photo--tent    { left: 148px; top: 1px;  width: 70px;  height: 91px; background: var(--photo-tent); }
  .photo--lane    { left: 220px; top: 1px;  width: 70px;  height: 91px; background: var(--photo-lane); }
  .photo--chapel  { left: 4px;   top: 94px; width: 70px;  height: 92px; background: var(--photo-chapel); }
  .photo--bouquet { left: 76px;  top: 94px; width: 70px;  height: 92px; background: var(--photo-bouquet); }
  .photo--beach   { left: 148px; top: 94px; width: 142px; height: 92px; background: var(--photo-beach); }

  /* Back */
  .back-mark {
    position: absolute; left: 30px; top: 34px;
    width: 93px; height: 73px;
    background: var(--panel);
  }
  .back-mark__square {
    position: absolute; left: 16px; top: 7px;
    width: 62px; height: 62px;
    background: var(--mark);
  }
  .contact-panel {
    position: absolute; left: 184px; top: 192px;
    width: 298px; height: 187px;
    background: var(--card);
  }
  .contact-name {
    position: absolute; left: 10px; top: 8px;
    width: 272px; height: 33px;
    background: var(--panel);
    font-family: "Josefin Sans", sans-serif; font-weight: 300;
    font-size: 24px; letter-spacing: 4.5px; line-height: 33px;
    padding-left: 8px; white-space: nowrap;
  }
  .contact-list { position: absolute; left: 20px; top: 53px; list-style: none; }
  .contact-list li {
    display: flex; align-items: center;
    height: 31.5px; font-size: 17px; white-space: nowrap;
  }
  .contact-list svg { width: 28px; height: 26px; margin-right: 15px; fill: none; stroke: var(--mark); flex: none; }
</style>
</head>
<body>

<section class="card card--front">
  <div class="band"></div>
  <div class="brand-block">
    <div class="brand-square"></div>
    <div class="brand-name">COLBY VARNWAY</div>
    <div class="brand-tag">PHOTOGRAPHERS</div>
  </div>
  <div class="gallery">
    <div class="gallery__photo photo--garden" role="img" aria-label="Wedding couple beside a vintage car in a garden"></div>
    <div class="gallery__photo photo--tent" role="img" aria-label="Long reception table under a white draped tent"></div>
    <div class="gallery__photo photo--lane" role="img" aria-label="Couple walking down a cypress-lined path"></div>
    <div class="gallery__photo photo--chapel" role="img" aria-label="Outdoor ceremony aisle leading to a chapel"></div>
    <div class="gallery__photo photo--bouquet" role="img" aria-label="Bridal bouquet of peach and white flowers"></div>
    <div class="gallery__photo photo--beach" role="img" aria-label="Wedding couple on a beach by the sea"></div>
  </div>
</section>

<section class="card card--back">
  <div class="back-mark"><div class="back-mark__square"></div></div>
  <div class="band"></div>
  <div class="contact-panel">
    <div class="contact-name">COLBY VARNWAY</div>
    <ul class="contact-list">
      <li>
        <svg viewBox="0 0 28 26" aria-hidden="true"><rect x="6" y="1" width="14" height="24" rx="3" stroke-width="2" transform="rotate(-12 13 13)"/></svg>
        5208813047
      </li>
      <li>
        <svg viewBox="0 0 28 26" aria-hidden="true"><circle cx="14" cy="13" r="4" stroke-width="2"/><path d="M18 9v6c0 2 3 2 3-1a8 8 0 1 0-3 6" stroke-width="2"/></svg>
        website/blog
      </li>
      <li>
        <svg viewBox="0 0 28 26" aria-hidden="true"><rect x="2" y="6" width="24" height="15" stroke-width="2"/><path d="M2 6l12 9 12-9M2 21l9-7M26 21l-9-7" stroke-width="2"/></svg>
        Email
      </li>
      <li>
        <svg viewBox="0 0 28 26" aria-hidden="true"><circle cx="14" cy="13" r="10" fill="#6f6f71" stroke="none"/></svg>
        Social username
      </li>
    </ul>
  </div>
</section>

</body>
</html>
```